Real Estate Agency Chatterlane Cover Photo

We need a Chatterlane cover photo created for our Real Estate Business. We also need this cover photo adapted to several other platforms. Please read this brindlo doc for full specifications of the job https://files.brindlo-example.net/sheet/d/8QwerPLm4ZxVb2NnKs7RtYhUe3_gHdjAoFcWsMvBn/view?mode=share

Please also carefully read the Must Haves/Should Not Haves

Please contact me if you have any queries. Looking forward to seeing your designs!

Owen

Industry/Entity Type

Real Estate Agent

Requirements
Must have
• The Taglines 'More Money In Your Pocket' and sub tagline 'With Our Low Flat Fee To Sell Your Home'

It can then also have other elements e.g our logo, contact details and anything else you think will work well.

It must also have great graphic design work which looks custom and very clean/modern
Should not have
• Must not have poor quality stock images or anything tacky regarding money etc

```html
<!DOCTYPE html>
<html lang="en">
<head>
<meta charset="utf-8">
<title>Norvale – Cover Banner</title>
<link rel="stylesheet" href="https://fonts.googleapis.com/css2?family=Open+Sans:wdth,wght@75..100,300..700&display=swap">
<style>
  :root {
    --stage: #a9abad;
    --paper: #f1f1f2;
    --paper-shade: #e2e2e4;
    --ink: #1e1e1f;
    --red: #d71920;
    --red-deep: #8e0f15;
    --red-dark: #6e0a10;
    --slate: #3b3c3d;
    --white: #ffffff;
    --photo-a: #7d8a4e;
    --photo-b: #4e5a2e;
    --photo-c: #c9cdb8;
  }
  html, body {
    margin: 0;
    width: 1200px;
    height: 960px;
    overflow: hidden;
    background: var(--stage);
  }
  .cover {
    position: absolute;
    left: 40px;
    top: 272px;
    width: 1120px;
    height: 415px;
    box-shadow: 0 18px 40px rgba(0,0,0,.25);
  }
  .cover svg { display: block; }
  .txt { font-family: "Open Sans", sans-serif; }
  .narrow { font-stretch: 75%; }
  .brand { fill: var(--red); font-weight: 600; font-size: 70px; letter-spacing: 2px; }
  .tagline { fill: var(--white); font-weight: 400; font-size: 31px; }
  .subtagline { fill: var(--red); font-weight: 400; font-size: 19px; }
  .web { fill: var(--white); font-weight: 400; font-size: 27px; }
  .call-title { fill: var(--white); font-weight: 600; font-size: 26px; }
  .call-number { fill: var(--red); font-weight: 400; font-size: 16px; }
  .steps-title { fill: var(--white); font-weight: 400; font-size: 20px; }
  .steps-list { fill: var(--white); font-weight: 400; font-size: 12px; }
</style>
</head>
<body>
<div class="cover">
  <svg width="1120" height="415" viewBox="0 0 1120 415" xmlns="http://www.w3.org/2000/svg">
    <defs>
      <linearGradient id="paperTone" x1="0" y1="0" x2="1" y2="1">
        <stop offset="0" stop-color="var(--paper)"/>
        <stop offset="1" stop-color="var(--paper-shade)"/>
      </linearGradient>
      <linearGradient id="photoTone" x1="0" y1="0" x2="1" y2="1">
        <stop offset="0" stop-color="var(--photo-c)"/>
        <stop offset=".35" stop-color="var(--photo-a)"/>
        <stop offset="1" stop-color="var(--photo-b)"/>
      </linearGradient>
      <linearGradient id="webBand" x1="0" y1="1" x2="1" y2="0">
        <stop offset="0" stop-color="var(--red-deep)"/>
        <stop offset=".55" stop-color="var(--red-deep)"/>
        <stop offset="1" stop-color="var(--red)"/>
      </linearGradient>
      <linearGradient id="stepsBand" x1="0" y1="1" x2="1" y2="0">
        <stop offset="0" stop-color="var(--red-dark)"/>
        <stop offset=".5" stop-color="var(--red-deep)"/>
        <stop offset="1" stop-color="var(--red)"/>
      </linearGradient>
    </defs>

    <!-- paper background -->
    <rect class="paper" width="1120" height="415" fill="url(#paperTone)"
          role="img" aria-label="Light grey geometric cube pattern"/>

    <!-- photo area -->
    <polygon class="photo" points="470,0 1120,0 1120,415 770,415"
             fill="url(#photoTone)" role="img"
             aria-label="Photo of the two agents standing outdoors above a wooded valley"/>

    <!-- top-right contact corner -->
    <polygon class="call-corner" points="820,0 1120,0 1120,20 980,72 860,72" fill="var(--slate)" opacity=".85"/>

    <!-- small red accent wedge -->
    <polygon class="accent-wedge" points="455,0 540,0 500,58 440,58" fill="var(--red)"/>

    <!-- black message panel -->
    <polygon class="message-panel" points="0,58 500,58 770,270 770,290 430,345 0,345" fill="var(--ink)"/>

    <!-- red web band -->
    <polygon class="web-band" points="400,292 770,270 770,352 600,402 430,345" fill="url(#webBand)"/>

    <!-- steps band -->
    <polygon class="steps-band" points="770,270 1120,230 1120,415 770,415" fill="url(#stepsBand)"/>
    <rect class="steps-edge" x="770" y="270" width="10" height="145" fill="var(--red-dark)" opacity=".6"/>

    <!-- brand -->
    <text class="txt brand" x="90" y="175">NORVALE</text>

    <!-- taglines -->
    <text class="txt tagline" x="90" y="225">More Money In Your Pocket</text>
    <rect class="subtag-box" x="90" y="240" width="400" height="32" fill="var(--white)"/>
    <text class="txt subtagline" x="102" y="263">With Our Low Flat Fee To Sell Your Home</text>

    <!-- web address -->
    <text class="txt web" x="595" y="340" text-anchor="middle" textLength="330" lengthAdjust="spacingAndGlyphs">www.norvale-homes.example</text>

    <!-- call us -->
    <text class="txt narrow call-title" x="1010" y="34" text-anchor="middle">Call Us</text>
    <text class="txt call-number" x="1010" y="56" text-anchor="middle">+61 2 5550 0147</text>

    <!-- steps -->
    <text class="txt narrow steps-title" x="950" y="322" text-anchor="middle">5 EASY STEPS TO SELL YOUR HOME</text>
    <text class="txt narrow steps-list" x="950" y="352" text-anchor="middle" textLength="320" lengthAdjust="spacingAndGlyphs">APPRAISAL | ENGAGEMENT | ADVERTISEMENT | INSPECTIONS | SETTLEMENT</text>
  </svg>
</div>
</body>
</html>
```